Brambleway Business Card

I have a business that is called "Brambleway Electrical Goods LTD" My company deals with top of the range laptops and mobile phones that are exclusive. I need a business card that will be eye catching but not over complicated.

Target Market(s)

Adults aged 19 to 50
Upper middle class

Industry/Entity Type

Business

Requirements
Must have
• Company name/logo (file attached)
• It must have my contact information which is:

• Name: Dale Margrove

• Position: Managing Director 

• Business Address: 7 Haddon Row, London, W4 9QZ

• Contact Number: 02085519304
• Mobile: 07815206473
• Email: info@brambleway-goods.co.uk
Nice to have
• Simple and stylish
• Eye catching

```html
<!DOCTYPE html>
<html lang="en">
<head>
<meta charset="utf-8">
<title>Brambleway Business Card</title>
<link rel="stylesheet" href="https://fonts.googleapis.com/css2?family=Quicksand:wght@300;400;700&display=swap">
<style>
  :root {
    --page: #fefefe;
    --card: #201c1a;
    --ink: #ffffff;
    --brand: #72c0ea;
    --accent: #0a86c8;
  }
  * { margin: 0; padding: 0; box-sizing: border-box; }
  html, body {
    width: 1200px;
    height: 849px;
    overflow: hidden;
    background: var(--page);
  }
  .business-card {
    position: absolute;
    left: 197px;
    top: 177px;
    width: 783px;
    height: 479px;
    background: var(--card);
    font-family: "Quicksand", sans-serif;
    color: var(--ink);
  }
  .brand-name {
    position: absolute;
    left: 34px;
    top: 28px;
    font-size: 56px;
    font-weight: 400;
    letter-spacing: 2px;
    line-height: 1;
    color: var(--brand);
  }
  .person {
    position: absolute;
    left: 354px;
    top: 188px;
  }
  .person-name {
    font-size: 30px;
    font-weight: 700;
    letter-spacing: 1.5px;
    line-height: 34px;
  }
  .person-role {
    font-size: 27px;
    font-weight: 400;
    letter-spacing: 1.8px;
    line-height: 32px;
  }
  .divider {
    position: absolute;
    left: 355px;
    right: 0;
    top: 280px;
    height: 1px;
    background: var(--accent);
  }
  .contact {
    position: absolute;
    left: 354px;
    top: 318px;
    list-style: none;
    font-size: 26px;
    font-weight: 400;
    letter-spacing: 2px;
    line-height: 31.5px;
  }
  .phone-split {
    display: inline-block;
    width: 3px;
    height: 21px;
    margin: 0 9px 0 4px;
    background: var(--accent);
    border-radius: 1.5px;
    vertical-align: -2px;
  }
</style>
</head>
<body>
  <article class="business-card">
    <div class="brand-name">Brambleway</div>

    <header class="person">
      <h1 class="person-name">Dale Margrove</h1>
      <p class="person-role">Managing Director</p>
    </header>

    <div class="divider"></div>

    <ul class="contact">
      <li class="contact-street">7 Haddon Row,</li>
      <li class="contact-city">London, W4 9QZ</li>
      <li class="contact-phones">02085519304<span class="phone-split"></span>07815206473</li>
      <li class="contact-email">info@brambleway-goods.co.uk</li>
    </ul>
  </article>
</body>
</html>
```